Boutique Real Estate Brokerage Ambrel Realty Website Design

Winning designer work on migrate as well through net pilvo.
We need a new website as an informational hub to aid our print and digital strategy as well as showing that we are located in Brooklyn and Florida. I have a boutique real estate brokerage and advisory firm specializing in residential leasing, multifamily sales and 1031 Exchange appropriation. This won't be a portal to search properties, it will be a place for information. I'd like space for an ebook to be downloaded and information on my probate sales and multifamily leasing marketing campaigns. I included my logo and will leave it up to the designer to come up with colors to match it. I have also attached verbiage for each page. The final design should have a modern high end look that reflects gentrifying Brooklyn as well as beautiful Florida.
Thank you!
Target Market(s)
Owners of income producing real estate and develop-able land in Brooklyn, NY and Florida.
Industry/Entity Type
Real Estate
Coding
Coded - Design and coding required
Number of Pages Required
5+ page
Colors
Designer to choose colors to be used in the design.
Requirements
Must have
- A modern elegant look
Nice to have
- pictures of brooklyn and florida
Should not have
- real estate search pages

```html
<!DOCTYPE html>
<html lang="en">
<head>
<meta charset="utf-8">
<title>Ambrel Realty</title>
<link href="https://fonts.googleapis.com/css2?family=Open+Sans:ital,wght@0,400;0,600;1,400&family=Roboto+Slab:wght@300;400&display=swap" rel="stylesheet">
<style>
:root{
  --black:#000;
  --white:#fff;
  --ink:#333;
  --muted:#555;
  --orange:#f47a12;
  --band:#4a4a4a;
  --soft:#f3f3f3;
  --line:#cfcfcf;
  --rule:#999;
}
*{margin:0;padding:0;box-sizing:border-box}
html,body{width:1200px;height:3046px;overflow:hidden}
body{position:relative;background:var(--white);font-family:"Open Sans",sans-serif;color:var(--ink)}
.abs{position:absolute}
.slab{font-family:"Roboto Slab",serif}

/* header */
.site-header{left:0;top:0;width:1200px;height:122px;background:var(--black)}
.brand{display:flex;align-items:center;gap:14px;color:var(--white);font-family:"Roboto Slab",serif;font-weight:400;font-size:19px;letter-spacing:2px;text-transform:uppercase}
.brand-mark{width:44px;height:44px;background:#8a8a8a}
.site-header .brand{left:112px;top:38px}
.call{right:112px;top:14px;display:flex;align-items:center;gap:14px;color:var(--white);font-family:"Roboto Slab",serif;font-size:16px}
.call-icon{width:46px;height:46px;border:1px solid #777;border-radius:50%;display:flex;align-items:center;justify-content:center}
.main-nav{right:112px;top:80px;display:flex;gap:50px;font-family:"Roboto Slab",serif;font-size:12px;color:var(--white);letter-spacing:.5px}

/* hero */
.hero{left:0;top:122px;width:1200px;height:678px;overflow:hidden}
.hero-photo{position:absolute;inset:0;background:linear-gradient(180deg,#6d8fb8 0%,#9fb6cf 22%,#b9804f 32%,#8a5a3e 40%,#4d7a3a 48%,#3e5f35 52%,#5c6f7d 60%,#34404a 100%)}
.hero-title{left:0;width:1200px;text-align:center;color:var(--white);font-family:"Roboto Slab",serif;font-weight:300;text-shadow:0 1px 3px rgba(0,0,0,.4)}
.hero-title .l1{font-size:32px;display:block;margin-bottom:6px}
.hero-title .l2{font-size:38px;display:block}
.btn-orange{background:var(--orange);color:var(--white);border-radius:28px;font-family:"Roboto Slab",serif;font-size:18px;display:flex;align-items:center;justify-content:center}
.arrow-btn{width:32px;height:32px;border:2px solid var(--white);border-radius:50%;display:flex;align-items:center;justify-content:center}

/* sections */
.section-title{left:0;width:1200px;text-align:center;font-family:"Roboto Slab",serif;font-weight:300;font-size:34px;color:#444}
.title-rule{left:556px;width:88px;height:2px;background:var(--rule)}
.service-photo{width:313px;height:236px}
.service-name{width:313px;text-align:center;font-family:"Roboto Slab",serif;font-size:18px;color:#222}
.service-text{width:313px;text-align:center;font-style:italic;font-size:11.5px;line-height:27px;color:var(--muted);padding:0 14px}

.split-left{left:0;top:1357px;width:592px;height:475px;background:var(--band)}
.split-photo{left:592px;top:1357px;width:608px;height:475px;background:linear-gradient(180deg,#2f4d8f 0%,#6a78b0 30%,#d79a7a 48%,#3a3f5a 58%,#1d6fb0 72%,#0f3f7c 100%)}
.split-heading{left:112px;top:1444px;width:460px;color:var(--white);font-family:"Roboto Slab",serif;font-weight:300;font-size:21px;line-height:42px}
.split-text{left:112px;top:1548px;width:445px;color:#ddd;font-style:italic;font-size:11.5px;line-height:27px}
.btn-ghost-light{left:112px;top:1698px;width:178px;height:54px;border:1.5px solid var(--white);border-radius:28px;color:var(--white);font-family:"Roboto Slab",serif;font-size:17px;display:flex;align-items:center;justify-content:center}

.tool-circle{width:134px;height:134px;border:1.5px solid var(--line);border-radius:50%;display:flex;align-items:center;justify-content:center}
.tool-name{width:334px;text-align:center;font-family:"Roboto Slab",serif;font-weight:300;font-size:19px;color:#222}
.tool-text{width:334px;text-align:center;font-style:italic;font-size:11.5px;line-height:27px;color:var(--muted);padding:0 40px}

.ebook{left:0;top:2260px;width:1200px;height:372px;background:var(--soft)}
.ebook-cover{left:190px;top:2290px;width:300px;height:320px;background:linear-gradient(135deg,#2f2e88 0%,#1f1d66 70%,#f47a12 71%,#f47a12 100%)}
.ebook-heading{left:530px;top:2318px;width:560px;font-family:"Roboto Slab",serif;font-weight:300;font-size:28px;line-height:48px;color:#333}
.ebook-text{left:530px;top:2420px;width:540px;font-style:italic;font-size:11.5px;line-height:27px;color:var(--muted)}
.btn-ghost-dark{left:530px;top:2510px;width:210px;height:56px;border:1.5px solid #bbb;border-radius:28px;color:#444;font-family:"Roboto Slab",serif;font-size:17px;display:flex;align-items:center;justify-content:center}

/* footer */
.site-footer{left:0;top:2632px;width:1200px;height:414px;background:var(--black)}
.site-footer .brand{left:0;width:1200px;top:2676px;justify-content:center}
.footer-rule{left:112px;width:976px;height:1px;background:#333}
.foot-icon{width:64px;height:64px;border:1.5px solid #ccc;border-radius:50%;display:flex;align-items:center;justify-content:center}
.foot-label{width:300px;text-align:center;color:var(--white);font-family:"Roboto Slab",serif;font-size:16px;letter-spacing:.5px}
.foot-text{width:300px;text-align:center;color:#bbb;font-size:11.5px;line-height:25px}
.copyright{left:0;width:1200px;top:2996px;text-align:center;color:#ccc;font-size:12px}
</style>
</head>
<body>

<header class="abs site-header">
  <div class="abs brand"><span class="brand-mark"></span>Ambrel Realty</div>
  <div class="abs call">
    <span class="call-icon"><svg width="18" height="18" viewBox="0 0 24 24"><path fill="#fff" d="M6.6 10.8a15.1 15.1 0 0 0 6.6 6.6l2.2-2.2c.3-.3.7-.4 1-.2 1.1.4 2.3.6 3.6.6.6 0 1 .4 1 1V20c0 .6-.4 1-1 1A17 17 0 0 1 3 4c0-.6.4-1 1-1h3.5c.6 0 1 .4 1 1 0 1.2.2 2.4.6 3.6.1.3 0 .7-.2 1z"/></svg></span>
    Call Us : 516-480-2217
  </div>
  <nav class="abs main-nav"><span>HOME</span><span>ABOUT US</span><span>SERVICES</span><span>SIGN UP</span><span>CONTACT</span></nav>
</header>

<section class="abs hero">
  <div class="hero-photo" role="img" aria-label="Waterfront apartment complex with palm trees and a fountain reflecting in a lake"></div>
  <div class="abs arrow-btn" style="left:66px;top:330px"><svg width="12" height="12" viewBox="0 0 12 12"><path d="M8 1 3 6l5 5" stroke="#fff" stroke-width="2" fill="none"/></svg></div>
  <div class="abs arrow-btn" style="left:1096px;top:330px"><svg width="12" height="12" viewBox="0 0 12 12"><path d="M4 1l5 5-5 5" stroke="#fff" stroke-width="2" fill="none"/></svg></div>
  <h1 class="abs hero-title" style="top:410px"><span class="l1">Assisting landlords increase</span><span class="l2">profits while decreasing the stress</span></h1>
  <div class="abs btn-orange" style="left:512px;top:530px;width:176px;height:54px">Read More</div>
  <svg class="abs" style="left:0;top:0" width="1200" height="678" viewBox="0 0 1200 678">
    <polygon points="0,530 600,660 1200,530 1200,678 0,678" fill="#3a3a3a"/>
    <polygon points="0,544 600,670 1200,544 1200,678 0,678" fill="#fff"/>
  </svg>
</section>

<h2 class="abs section-title" style="top:830px">How We Can Help</h2>
<div class="abs title-rule" style="top:890px"></div>

<div class="abs service-photo" style="left:112px;top:928px;background:linear-gradient(160deg,#e9e9e6,#b9bcb8 60%,#8b8175)" role="img" aria-label="Bright modern apartment kitchen and dining area"></div>
<div class="abs service-photo" style="left:444px;top:928px;background:linear-gradient(160deg,#8a6f55,#5c4738 60%,#2f2a26)" role="img" aria-label="Brick multifamily building facade with fire escapes"></div>
<div class="abs service-photo" style="left:776px;top:928px;background:linear-gradient(180deg,#a9c3dc,#6e8a6a 35%,#4d6a48 70%,#3f5a6a)" role="img" aria-label="Aerial view of land and a lake for site selection"></div>

<h3 class="abs service-name" style="left:112px;top:1188px">Multi-Family Leasing</h3>
<h3 class="abs service-name" style="left:444px;top:1188px">Multi-Family Sales</h3>
<h3 class="abs service-name" style="left:776px;top:1188px">Site Selection Advisory</h3>
<p class="abs service-text" style="left:112px;top:1228px">Ambrel Realty NYC is a full service real estate brokerage firm located in Brooklyn, NY and West 1031 Exchange property appropriation.</p>
<p class="abs service-text" style="left:444px;top:1228px">Ambrel Realty NYC is a full service real estate brokerage firm located in Brooklyn, NY and West 1031 Exchange property appropriation.</p>
<p class="abs service-text" style="left:776px;top:1228px">Ambrel Realty NYC is a full service real estate brokerage firm located in Brooklyn, NY and West 1031 Exchange property appropriation.</p>

<div class="abs split-left"></div>
<div class="abs split-photo" role="img" aria-label="City skyline at dusk reflected in the water"></div>
<h2 class="abs split-heading">Brooklyn, NY To West Palm Beach Florida....<br>The Best Of Both Worlds</h2>
<p class="abs split-text">Ambrel Realty NYC is a full service real estate brokerage firm located in Brooklyn, NY and West Palm Beach, FL. We specialize in multifamily sales and leasing; short-sales and 1031 Exchange property appropriation. With more than 12 years of experience of Brooklyn's zip codes, but specialize in Northern...</p>
<div class="abs btn-ghost-light">Read More</div>

<h2 class="abs section-title" style="top:1864px">Mortgage Tools</h2>

<div class="abs tool-circle" style="left:198px;top:1966px"><svg width="52" height="52" viewBox="0 0 52 52" fill="none" stroke="#555" stroke-width="1.6"><path d="M4 48h44M8 48V36h7v12M20 48V28h7v12M32 48V22h7v26M10 22l10-8 8 5 14-12"/><path d="M36 7h6v6"/></svg></div>
<div class="abs tool-circle" style="left:533px;top:1966px"><svg width="52" height="52" viewBox="0 0 52 52" fill="none" stroke="#555" stroke-width="1.6"><rect x="12" y="6" width="28" height="42" rx="2"/><rect x="17" y="11" width="18" height="8"/><path d="M17 25h4v4h-4zM24 25h4v4h-4zM31 25h4v4h-4zM17 32h4v4h-4zM24 32h4v4h-4zM31 32h4v4h-4zM17 39h4v4h-4zM24 39h4v4h-4zM31 39h4v4h-4z"/></svg></div>
<div class="abs tool-circle" style="left:868px;top:1966px"><svg width="52" height="52" viewBox="0 0 52 52" fill="none" stroke="#555" stroke-width="1.6"><path d="M26 40S14 27 14 18a12 12 0 0 1 24 0c0 9-12 22-12 22z"/><circle cx="26" cy="18" r="4"/><path d="M12 36 4 48h44l-8-12"/></svg></div>

<h3 class="abs tool-name" style="left:98px;top:2114px">Mortgage Rates</h3>
<h3 class="abs tool-name" style="left:433px;top:2114px">Mortgage Calculator</h3>
<h3 class="abs tool-name" style="left:768px;top:2114px">Coverage Areas</h3>
<p class="abs tool-text" style="left:98px;top:2152px">Ambrel Realty NYC specializes in assisting landlords profits while decreasing their stress.</p>
<p class="abs tool-text" style="left:433px;top:2152px">Ambrel Realty NYC specializes in assisting landlords profits while decreasing their stress.</p>
<p class="abs tool-text" style="left:768px;top:2152px">Ambrel Realty NYC specializes in assisting landlords profits while decreasing their stress.</p>

<section class="abs ebook"></section>
<div class="abs ebook-cover" role="img" aria-label="Ebook cover with a download badge"></div>
<h2 class="abs ebook-heading">ebook for probate sales &amp;<br>multifamily leasing marketing campaigns</h2>
<p class="abs ebook-text">Ambrel Realty NYC specializes in assisting landlords by increasing their profits while decreasing their stress.With more than 12 years of experience we have had transactions</p>
<div class="abs btn-ghost-dark">Download Now!</div>

<footer class="abs site-footer"></footer>
<div class="abs brand" style="left:0;width:1200px;top:2676px;justify-content:center"><span class="brand-mark"></span>Ambrel Realty</div>
<div class="abs footer-rule" style="top:2757px"></div>

<div class="abs foot-icon" style="left:250px;top:2780px"><svg width="20" height="20" viewBox="0 0 24 24"><path fill="#fff" d="M12 2a7 7 0 0 0-7 7c0 5 7 13 7 13s7-8 7-13a7 7 0 0 0-7-7zm0 9.5A2.5 2.5 0 1 1 12 6.5a2.5 2.5 0 0 1 0 5z"/></svg></div>
<div class="abs foot-icon" style="left:583px;top:2780px"><svg width="18" height="18" viewBox="0 0 24 24"><path fill="#fff" d="M6.6 10.8a15.1 15.1 0 0 0 6.6 6.6l2.2-2.2c.3-.3.7-.4 1-.2 1.1.4 2.3.6 3.6.6.6 0 1 .4 1 1V20c0 .6-.4 1-1 1A17 17 0 0 1 3 4c0-.6.4-1 1-1h3.5c.6 0 1 .4 1 1 0 1.2.2 2.4.6 3.6.1.3 0 .7-.2 1z"/></svg></div>
<div class="abs foot-icon" style="left:913px;top:2780px"><svg width="18" height="18" viewBox="0 0 24 24"><path fill="#fff" d="M2 5h20v2l-10 6L2 7zm0 4 10 6 10-6v10H2z"/></svg></div>

<h4 class="abs foot-label" style="left:132px;top:2864px">LOCATION</h4>
<h4 class="abs foot-label" style="left:465px;top:2864px">CONTACT</h4>
<h4 class="abs foot-label" style="left:795px;top:2864px">EMAIL</h4>
<p class="abs foot-text" style="left:132px;top:2892px">482 Halvern Ave, 2, Brooklyn,<br>New York 11216</p>
<p class="abs foot-text" style="left:465px;top:2892px">Phone : 561-730-4496</p>
<p class="abs foot-text" style="left:795px;top:2892px">hello@ambrelnycrealty.com</p>

<div class="abs footer-rule" style="top:2967px"></div>
<p class="abs copyright">© Copyright 2019 Ambrel Realty.All rights reserved.</p>

</body>
</html>
```